Website design for a Fine Food exhibition in Asia

We need a website design for a Food and Wine exhibition (home page). The name of the exhibition is "Platara" which is going to be Held in south korea. The concept is "Fine Food" in major, qui means clustering Would not we accept Any canned food, fast food, chips, thesis kind of foods. We do not open to the public like Some Other Food exhibitions do, Then only trade visitors. The EXHIBITORS will come from all the World. The categories we Would like to make is in attachment below. We will update the text When the category's share will be done. We need a color can qui correspond well to the "Find Food ', color of our logo qui est in attachment Would be good. You can offer us some photos, images, like photos of fine food corners in supermarkets, gourmet shops like photos of etc. ... You can find links Some of "same" exhibitions in below, qui can give you a guideline of the kind of website we expect. http://en.vitrine-delices-choix.example/ http://marblerootfair.example/ http: //www.tideplatenexpo. example.kr We will ask to the winning designer to Develop the full website under Wordpress.

Target Market(s)

Fine food, gourmet food, "grocery", pastry, bakery

Number of Pages Required

5+ page

Font styles to use
Sans Serif

Colors
886aae
6b449b
e34197
e667a6
9bcb3c
f58947
f37122
ec1f27

Requirements
Must have
• Warm colors, and layout showing the high level of foods, fine foods, gourmet foods
Nice to have
• It would be nice to include the sentence "The new meeting place for the gourmet food in Asia"

```html
<!DOCTYPE html>
<html lang="en">
<head>
<meta charset="utf-8">
<title>Platara – The Fine Food Event in Asia</title>
<link href="https://fonts.googleapis.com/css2?family=Crimson+Text:wght@400;600&family=PT+Sans:wght@400;700&family=Arimo:wght@400;700&display=swap" rel="stylesheet">
<style>
  :root {
    --plum: #8a1f5c;
    --plum-dark: #7a1049;
    --rose: #c0404f;
    --rose-dark: #a8343f;
    --aubergine: #3b1d3a;
    --aubergine-dark: #2e1530;
    --accent-red: #c8102e;
    --link-red: #b2162a;
    --salmon: #f58947;
    --text: #333;
    --muted: #8b8b8b;
    --nav: #9a8f86;
    --footer: #333;
    --footer-top: #555;
    --footer-text: #bbb;
    --dotted: #999;
    --white: #fff;
  }
  * { box-sizing: border-box; margin: 0; padding: 0; }
  html, body { width: 979px; height: 1200px; overflow: hidden; background: var(--white); }
  body { position: relative; font-family: "Arimo", Arial, sans-serif; color: var(--text); }
  .abs { position: absolute; }
  a { color: inherit; }

  /* header */
  .brand { left: 72px; top: 22px; display: flex; align-items: center; gap: 10px; }
  .brand-mark { width: 16px; height: 16px; border-radius: 50%; background: var(--plum); }
  .brand-name { font-family: "Crimson Text", Georgia, serif; font-size: 40px; color: var(--plum); line-height: 1; letter-spacing: 1px; }
  .brand-tag { left: 72px; top: 68px; font-family: "Arimo", Arial, sans-serif; font-size: 14px; color: var(--plum); font-weight: 700; }
  .main-nav { right: 34px; top: 66px; display: flex; gap: 12px; font-family: "Crimson Text", Georgia, serif; font-size: 17px; color: var(--nav); letter-spacing: .5px; }
  .main-nav span.sep { color: #bbb; }
  .header-shade { left: 0; top: 0; width: 979px; height: 100px; background: linear-gradient(#ececec, #fff 60%); z-index: -1; }

  /* hero */
  .hero { left: 35px; top: 107px; width: 910px; height: 396px; display: flex; }
  .hero-card { width: 303.4px; display: flex; flex-direction: column; }
  .hero-card .topband { height: 9px; }
  .hero-card .photo { height: 289px; }
  .hero-card h2 { height: 62px; padding: 12px 0 0 12px; font-family: "Crimson Text", Georgia, serif; font-weight: 400; font-size: 33px; color: var(--white); line-height: 1.1; }
  .hero-card .more { height: 36px; padding: 10px 0 0 12px; font-family: "Crimson Text", Georgia, serif; font-size: 13px; color: #f3e6e6; letter-spacing: .5px; }
  .c1 .topband { background: var(--rose); } .c1 h2 { background: var(--rose); } .c1 .more { background: var(--rose-dark); }
  .c2 .topband { background: var(--plum); } .c2 h2 { background: var(--plum); } .c2 .more { background: var(--plum-dark); }
  .c3 .topband { background: var(--aubergine); } .c3 h2 { background: var(--aubergine); } .c3 .more { background: var(--aubergine-dark); }
  .c1 .photo { background: radial-gradient(circle at 45% 45%, #f2c14a 0 10%, #c2431f 22%, #4a2a1c 55%, #d8d2c8 80%); }
  .c2 .photo { background: radial-gradient(circle at 50% 45%, #7a5a4a 0 20%, #3a2a24 40%, #9a4030 60%, #cfc6bc 85%); }
  .c3 .photo { background: radial-gradient(circle at 55% 60%, #b0302c 0 10%, #e4d4b0 25%, #6aa040 45%, #3a2a22 70%, #8a6a4a 100%); }

  .content-shade { left: 35px; top: 505px; width: 910px; height: 76px; background: linear-gradient(#e6e6e6, #fff); z-index: -1; }

  /* left column */
  .serif-link { font-family: "Crimson Text", Georgia, serif; font-size: 25px; color: var(--rose); line-height: 1.2; }
  .side-links { left: 44px; top: 528px; }
  .booth-title { left: 45px; top: 592px; font-size: 14px; font-weight: 700; color: var(--accent-red); }
  .booth-table { left: 44px; top: 630px; width: 234px; height: 82px; border: 1px solid #222; border-collapse: collapse; font-size: 12px; }
  .booth-table th { background: var(--salmon); color: var(--white); font-size: 14px; height: 30px; border: 1px solid #222; text-align: left; padding-left: 6px; }
  .booth-table th + th { text-align: center; }
  .booth-table td { border-right: 1px solid #222; padding: 2px 6px; height: 20px; vertical-align: top; }
  .booth-table td a { color: #444; }
  .visitors-title { left: 45px; top: 727px; font-family: "PT Sans", Arial, sans-serif; font-size: 24px; color: #333; }
  .visitor-list { left: 46px; top: 758px; list-style: none; font-family: "PT Sans", Arial, sans-serif; font-size: 11px; line-height: 12.3px; color: var(--muted); }
  .side-reg { left: 44px; top: 997px; }

  /* main column */
  .section-title { left: 348px; top: 526px; font-family: "Crimson Text", Georgia, serif; font-size: 42px; color: var(--plum); }
  .section-sub { left: 578px; top: 545px; font-family: "Crimson Text", Georgia, serif; font-size: 19px; color: #999; }
  .ambassador { left: 351px; top: 578px; width: 179px; height: 256px; background: linear-gradient(#e9e2e4 0%, #f0d6e4 50%, #2fb5a8 100%); }
  .dots { border-top: 1px dotted var(--dotted); }
  .dates { left: 502px; top: 602px; font-size: 15px; font-weight: 700; color: #555; line-height: 20px; }
  .venue { left: 552px; top: 666px; font-size: 11.5px; color: #555; line-height: 20px; }
  .info-links { left: 560px; top: 738px; list-style: none; font-size: 11.5px; }
  .info-links li { height: 25.5px; display: flex; align-items: center; gap: 12px; }
  .info-links a { color: var(--link-red); }
  .h3 { font-family: "Crimson Text", Georgia, serif; font-size: 25px; color: #333; }
  .feature-list { left: 350px; top: 890px; width: 262px; list-style: none; }
  .feature-list li { height: 64px; display: flex; align-items: center; gap: 12px; border-bottom: 1px dotted var(--dotted); font-size: 14.5px; font-weight: 700; }
  .feature-list li:last-child { border-bottom: none; }
  .feature-list .red { color: var(--accent-red); }
  .doc-illustration { left: 653px; top: 871px; width: 76px; height: 106px; border-radius: 6px; background: linear-gradient(135deg, #dfe8f4, #8fa8cc); }
  .useful { left: 747px; top: 870px; font-size: 12px; color: #555; line-height: 21px; }
  .useful .red { color: var(--accent-red); font-weight: 700; font-size: 15px; }
  .access { left: 649px; top: 1022px; font-size: 12px; line-height: 20px; color: #555; }
  .access .red { color: var(--accent-red); font-size: 11.5px; }

  /* footer */
  .footer { left: 0; top: 1107px; width: 979px; height: 93px; background: var(--footer); border-top: 6px solid var(--footer-top); text-align: center; font-size: 11.5px; color: var(--footer-text); padding-top: 33px; line-height: 18px; }
</style>
</head>
<body>
  <div class="abs header-shade"></div>
  <header>
    <div class="abs brand"><span class="brand-name">PLATARA</span><span class="brand-mark"></span></div>
    <div class="abs brand-tag">The Fine Food Event in Asia</div>
    <nav class="abs main-nav">
      <span>THE EXHIBITION</span><span class="sep">:</span>
      <span>EXHIBITORS</span><span class="sep">:</span>
      <span>VISITORS</span><span class="sep">:</span>
      <span>EVENTS</span><span class="sep">:</span>
      <span>MEDIA</span>
    </nav>
  </header>

  <section class="abs hero">
    <article class="hero-card c1">
      <div class="topband"></div>
      <div class="photo" role="img" aria-label="Stone bowl of bibimbap with fried egg and side dishes"></div>
      <h2>About Platara</h2>
      <div class="more">READ MORE &gt;&gt;</div>
    </article>
    <article class="hero-card c2">
      <div class="topband"></div>
      <div class="photo" role="img" aria-label="Korean table barbecue grill surrounded by side dishes"></div>
      <h2>Useful Information</h2>
      <div class="more">READ MORE &gt;&gt;</div>
    </article>
    <article class="hero-card c3">
      <div class="topband"></div>
      <div class="photo" role="img" aria-label="Hot pot with sliced vegetables, mushrooms and beef"></div>
      <h2>Floor Plan</h2>
      <div class="more">READ MORE &gt;&gt;</div>
    </article>
  </section>

  <div class="abs content-shade"></div>

  <aside>
    <div class="abs side-links serif-link">Exhibitors’ List<br>Contact us</div>
    <div class="abs booth-title">Booth Options</div>
    <table class="abs booth-table">
      <tr><th>Booth Type</th><th>Unit Price</th></tr>
      <tr><td><a href="#">Standard Booth</a></td><td></td></tr>
      <tr><td><a href="#">Premium Booth</a></td><td></td></tr>
    </table>
    <h3 class="abs visitors-title">Who are the visitors?</h3>
    <ul class="abs visitor-list">
      <li>Importer</li><li>Fine Food importers</li><li>Wine and Spirit importers</li><li>Beer importers</li>
      <li>Distributor</li><li>Fine Food distributors</li><li>Wine and Spirit distributors</li><li>Beer distributors</li>
      <li>Hotel and Restaurant</li><li>Chefs</li><li>Wine sommeliers</li><li>Retail</li>
      <li>Fine Food stores (ham, cheese, olive,</li><li>Wine and Spirit stores</li><li>Super/Hypermarket</li>
      <li>Fine Food categories</li><li>Department stores</li>
    </ul>
    <div class="abs side-reg serif-link">Visitor Registration<br>Asian VIP buyers program</div>
  </aside>

  <main>
    <h1 class="abs section-title">Fine Food</h1>
    <div class="abs section-sub">About Platara</div>
    <div class="abs ambassador" role="img" aria-label="Event ambassador in traditional hanbok"></div>
    <div class="abs dots" style="left:493px;top:591px;width:435px"></div>
    <div class="abs dates">Dates:<br>November 01-03, 2017</div>
    <div class="abs dots" style="left:493px;top:652px;width:435px"></div>
    <div class="abs venue">Venue :<br>HALLMONT Hall 8B<br>The professional B2B matching event to meet your partner</div>
    <ul class="abs info-links">
      <li><svg width="6" height="8" viewBox="0 0 6 8"><path d="M1 1l3 3-3 3" fill="none" stroke="#777"/></svg><a href="#">Texteà ajouter &nbsp; Texteà ajouter</a></li>
      <li><svg width="6" height="8" viewBox="0 0 6 8"><path d="M1 1l3 3-3 3" fill="none" stroke="#777"/></svg><a href="#">Texteà ajouter &nbsp; Texteà ajouter</a></li>
      <li><svg width="6" height="8" viewBox="0 0 6 8"><path d="M1 1l3 3-3 3" fill="none" stroke="#777"/></svg><a href="#">Texteà ajouter &nbsp; Texteà ajouter</a></li>
    </ul>

    <h3 class="abs h3" style="left:346px;top:836px">Floor Plan</h3>
    <ul class="abs feature-list">
      <li><svg width="36" height="34" viewBox="0 0 36 34"><rect x="2" y="4" width="26" height="28" fill="#d9d2c0" stroke="#9a8f7a"/><rect x="7" y="1" width="26" height="28" fill="#f3efe4" stroke="#9a8f7a"/><path d="M11 8h18M11 13h18M11 18h18M11 23h12" stroke="#b0a78f"/></svg><span class="red">Newsletter subscription</span></li>
      <li><svg width="36" height="34" viewBox="0 0 36 34"><rect x="2" y="4" width="26" height="28" fill="#d9d2c0" stroke="#9a8f7a"/><rect x="7" y="1" width="26" height="28" fill="#f3efe4" stroke="#9a8f7a"/><path d="M11 8h18M11 13h18M11 18h18M11 23h12" stroke="#b0a78f"/></svg><span>Who are the exhibitors?</span></li>
      <li><svg width="36" height="34" viewBox="0 0 36 34"><rect x="2" y="4" width="26" height="28" fill="#d9d2c0" stroke="#9a8f7a"/><rect x="7" y="1" width="26" height="28" fill="#f3efe4" stroke="#9a8f7a"/><path d="M11 8h18M11 13h18M11 18h18M11 23h12" stroke="#b0a78f"/></svg><span>Exhibitor Registration</span></li>
    </ul>

    <h3 class="abs h3" style="left:648px;top:836px">Useful Information</h3>
    <div class="abs doc-illustration" role="img" aria-label="Document with pen illustration"></div>
    <div class="abs useful">
      <span class="red">Date</span><br>
      <span class="red">02-03 November, 2017</span><br>
      Venue<br>
      HALLMONT HALL 8B<br>
      <a href="#">Opening Times</a><br>
      <a href="#">10:00 – 18:00 for the first day</a><br>
      <a href="#">10:00 – 17:00 for the second day</a>
    </div>
    <div class="abs access">
      <span class="red">Access to the Show</span><br>
      <a href="#" style="font-weight:700;margin-left:3px">HALLMONT</a><br>
      <a href="#" style="margin-left:3px">HALLMONT, Namsol-dong</a><br>
      <a href="#" style="margin-left:3px">Eunpa-gu, Harim-si, Gyeongdo-do, Korea</a>
    </div>
  </main>

  <footer class="abs footer">
    Home | Contact us | News | Partners | Press Release<br>
    Copyright © Platara
  </footer>
</body>
</html>
```